Business Cards and Company profile

I already have a company logo and website, I really need someone to come up with designs that are inkeeping with the theme of the website and the logo.
I need business cards and the company profile reworked (I areadly have the text) as described above.

thanks
Gareth
drifthavenvoyages.example

Target Market(s)

Mainly be for travel trade facing.

Industry/Entity Type

Business

```html
<!DOCTYPE html>
<html lang="en">
<head>
<meta charset="utf-8">
<title>Drifthaven Voyages – Business Card</title>
<link rel="stylesheet" href="https://fonts.googleapis.com/css2?family=Open+Sans:wght@400;600;700&family=Cormorant+Garamond:wght@500&display=swap">
<style>
  :root {
    --page-bg: #e4e3e3;
    --card-white: #ffffff;
    --card-edge: #d6d5d5;
    --brand-blue: #3a5fc8;
    --brand-blue-deep: #1c3585;
    --brand-navy: #1f3a8f;
    --brand-gold: #e9bd12;
    --text-light: #ffffff;
    --label-ink: #333333;
  }
  * { margin: 0; padding: 0; box-sizing: border-box; }
  html, body { width: 1200px; height: 765px; overflow: hidden; }
  body {
    position: relative;
    background: var(--page-bg);
    font-family: "Open Sans", Arial, sans-serif;
  }
  .card {
    position: absolute;
    top: 302px;
    width: 575px;
    height: 344px;
    border-radius: 43px;
    overflow: hidden;
  }
  .card-front {
    left: 16px;
    background: radial-gradient(ellipse at 50% 45%, #ffffff 40%, #eeeeee 100%);
    border: 1px solid var(--card-edge);
  }
  .front-brand {
    position: absolute;
    left: 0; right: 0;
    top: 152px;
    display: flex;
    justify-content: center;
    align-items: center;
    gap: 12px;
  }
  .brand-dot {
    width: 22px; height: 22px;
    border-radius: 50%;
    background: var(--brand-gold);
  }
  .front-brand-name {
    font-size: 26px;
    font-weight: 700;
    color: var(--brand-gold);
    letter-spacing: 0.5px;
  }

  .card-back {
    left: 604px;
    background: linear-gradient(160deg, var(--brand-blue) 30%, var(--brand-blue-deep) 100%);
  }
  .back-top-band {
    position: absolute; left: 0; right: 0; top: 0; height: 45px;
    background: var(--brand-blue);
  }
  .back-white-band {
    position: absolute; left: 0; right: 0; top: 45px; height: 59px;
    background: var(--card-white);
  }
  .back-rule {
    position: absolute; left: 0; right: 0; top: 104px; height: 4px;
    background: var(--brand-navy);
  }
  .back-gold-band {
    position: absolute; left: 0; right: 0; top: 108px; height: 19px;
    background: var(--brand-gold);
    border-bottom: 2px solid #f4dc6a;
  }
  .back-brand {
    position: absolute;
    left: 81px; top: 67px;
    display: flex; align-items: center; gap: 5px;
  }
  .back-brand .brand-dot { width: 10px; height: 10px; }
  .back-brand-name {
    font-size: 11px; font-weight: 700; color: var(--brand-gold);
  }
  .contact-block {
    position: absolute;
    left: 88px; top: 138px;
    color: var(--text-light);
  }
  .person-name { font-size: 25px; font-weight: 400; line-height: 1.1; }
  .person-role { font-size: 13.5px; margin-top: 2px; }
  .contact-list { list-style: none; margin-top: 14px; }
  .contact-list li {
    display: flex; align-items: center; gap: 8px;
    height: 19.5px;
    font-size: 12.5px;
  }
  .contact-list .num { letter-spacing: 2.4px; font-weight: 600; }
  .contact-list svg { width: 15px; height: 13px; fill: var(--text-light); flex: none; }
  .web { margin-top: 9px; font-size: 10.5px; letter-spacing: 2.2px; }

  .side-label {
    position: absolute;
    top: 684px;
    font-family: "Cormorant Garamond", Georgia, serif;
    font-size: 15px;
    letter-spacing: 3px;
    color: var(--label-ink);
  }
  .label-front { left: 66px; }
  .label-back { left: 659px; }
</style>
</head>
<body>
  <section class="card card-front">
    <div class="front-brand">
      <span class="brand-dot"></span>
      <span class="front-brand-name">DRIFTHAVEN VOYAGES</span>
    </div>
  </section>

  <section class="card card-back">
    <div class="back-top-band"></div>
    <div class="back-white-band"></div>
    <div class="back-rule"></div>
    <div class="back-gold-band"></div>
    <div class="back-brand">
      <span class="brand-dot"></span>
      <span class="back-brand-name">DRIFTHAVEN VOYAGES</span>
    </div>
    <div class="contact-block">
      <div class="person-name">Gareth Holloway</div>
      <div class="person-role">Managing Director</div>
      <ul class="contact-list">
        <li>
          <svg viewBox="0 0 16 13"><path d="M0 4 8 0l8 4v9H0z M1.5 4.5 8 8.5l6.5-4L8 1.5z" fill-rule="evenodd"/></svg>
          <span>gareth@drifthavenvoyages.example</span>
        </li>
        <li>
          <svg viewBox="0 0 16 13"><path d="M0 4c0-2 3-3 8-3s8 1 8 3v1h-4V3.5H4V5H0z M3 6h10l2 6H1z"/></svg>
          <span class="num">01632 960 418</span>
        </li>
        <li>
          <svg viewBox="0 0 16 13"><path d="M4 0h8v4H4z M1 5h14v8H1z M4 8h8v1H4z" fill-rule="evenodd"/></svg>
          <span class="num">01632 960 427</span>
        </li>
        <li>
          <svg viewBox="0 0 16 13"><path d="M1 1h14v12H1z M3 3h4v8H3z M9 3h4v2H9z M9 7h1.5v1.5H9z M11.5 7H13v1.5h-1.5z M9 9.5h1.5V11H9z M11.5 9.5H13V11h-1.5z" fill-rule="evenodd"/></svg>
          <span class="num">07700 900 362</span>
        </li>
      </ul>
      <div class="web">www.drifthavenvoyages.example</div>
    </div>
  </section>

  <div class="side-label label-front">FRONT</div>
  <div class="side-label label-back">BACK</div>
</body>
</html>
```